Business Card Design for Cybersecurity Company - Quorvent Systems

We need a business card design for our new cybersecurity company, Quorvent. We’re going for a clean, hi tech look that feels modern, premium, and trustworthy. We want a design that really stands out and makes people say WOW when we hand it over!

Quorvent delivers reliable IT support and managed services for small and mid sized businesses. We help companies stay secure, efficient, and connected through proactive monitoring, cybersecurity services, cloud management, and remote support.

Target Market(s)

Designers should target small and mid sized businesses that need dependable cybersecurity and IT support.

Industry/Entity Type

Cybersecurity, Managed Service Provider, IT services

Contact Information for Business Card

Contact information

Requirements
Must have
• The card should look clean, modern, and tech focused, with the Quorvent logo, clear contact info, and strong readability. It needs to feel premium and professional while still keeping a simple layout that fits a cybersecurity and IT brand.
Nice to have
• Nice to have elements include subtle touches that give the card a modern, tech feel, along with a layout that works well in different background styles.
Should not have
• The card should avoid clutter, loud graphics, or anything that takes attention away from the logo and contact details.

```html
<!DOCTYPE html>
<html lang="en">
<head>
<meta charset="utf-8">
<title>Quorvent Systems – Business Card</title>
<link rel="stylesheet" href="https://fonts.googleapis.com/css2?family=Poppins:wght@300;400;600&display=swap">
<style>
  :root {
    --page: #f2f2f2;
    --card: #000000;
    --panel: #3a3a3a;
    --violet: #7a2ff0;
    --blue: #3f8cf0;
    --white: #ffffff;
    --rule: #cfcfcf;
    --ink: #111111;
  }
  * { margin: 0; padding: 0; box-sizing: border-box; }
  html, body { width: 1200px; height: 849px; overflow: hidden; }
  body {
    background: var(--page);
    font-family: "Poppins", sans-serif;
    color: var(--white);
    position: relative;
  }
  .card {
    position: absolute;
    left: 322px;
    width: 556px;
    height: 317px;
    background: var(--card);
    overflow: hidden;
  }
  .card--front { top: 80px; }
  .card--back { top: 453px; }
  .card svg.decor { position: absolute; inset: 0; }

  .brand {
    position: absolute;
    display: flex;
    align-items: center;
    gap: 7px;
    font-weight: 400;
    color: var(--white);
    white-space: nowrap;
  }
  .brand__mark { display: block; }
  .card--front .brand {
    left: 50%; top: 156px;
    transform: translate(-50%, -50%);
    font-size: 22px;
  }
  .card--front .brand__mark { width: 22px; height: 22px; border: 2px solid var(--white); }
  .card--back .brand {
    right: 40px; top: 52px;
    transform: translateY(-50%);
    font-size: 16px;
  }
  .card--back .brand__mark { width: 16px; height: 16px; background: var(--violet); }

  .holder { position: absolute; left: 40px; top: 22px; }
  .holder__name {
    font-size: 29px;
    font-weight: 400;
    line-height: 1.1;
    letter-spacing: -0.3px;
    background: linear-gradient(90deg, var(--violet), var(--blue));
    -webkit-background-clip: text;
    background-clip: text;
    color: transparent;
    display: inline-block;
    border-bottom: 1.5px solid var(--blue);
    border-image: linear-gradient(90deg, var(--violet), var(--blue)) 1;
    padding-bottom: 1px;
  }
  .holder__role { font-size: 9.5px; font-weight: 300; margin-top: 6px; }

  .contacts { position: absolute; left: 40px; top: 150px; list-style: none; }
  .contact { display: flex; align-items: center; gap: 13px; height: 50px; }
  .contact__icon {
    width: 26px; height: 26px;
    background: var(--white);
    display: flex; align-items: center; justify-content: center;
  }
  .contact__label { font-size: 12px; font-weight: 600; line-height: 1.15; }
  .contact__value { font-size: 11px; font-weight: 300; line-height: 1.3; }
</style>
</head>
<body>

<section class="card card--front" aria-label="Card front">
  <svg class="decor" width="556" height="317" viewBox="0 0 556 317">
    <defs>
      <linearGradient id="frameGrad" x1="0" y1="1" x2="1" y2="0">
        <stop offset="0" stop-color="#7a2ff0"/>
        <stop offset="1" stop-color="#3f8cf0"/>
      </linearGradient>
    </defs>
    <polygon points="556,120 556,317 358,317" fill="#3a3a3a"/>
    <g fill="none" stroke="url(#frameGrad)" stroke-width="1.4">
      <polyline points="158,277 40,277 40,20 536,20 536,277"/>
      <polyline points="398,39 516,39 516,297 20,297 20,39"/>
    </g>
  </svg>
  <div class="brand"><span class="brand__mark"></span>Quorvent</div>
</section>

<section class="card card--back" aria-label="Card back">
  <svg class="decor" width="556" height="317" viewBox="0 0 556 317">
    <defs>
      <linearGradient id="tabGrad" x1="0" y1="0" x2="1" y2="0">
        <stop offset="0" stop-color="#7a2ff0"/>
        <stop offset="1" stop-color="#3f8cf0"/>
      </linearGradient>
    </defs>
    <polygon points="0,120 0,317 198,317" fill="#3a3a3a"/>
    <rect x="40" y="0" width="40" height="8" fill="url(#tabGrad)"/>
    <rect x="476" y="0" width="40" height="8" fill="url(#tabGrad)"/>
    <line x1="140" y1="94" x2="516" y2="94" stroke="#cfcfcf" stroke-width="1"/>
    <rect x="40" y="92.5" width="100" height="3" fill="url(#tabGrad)"/>
  </svg>

  <div class="holder">
    <h1 class="holder__name">Dorian Hale</h1>
    <p class="holder__role">Owner | CEO | Quorvent Systems</p>
  </div>

  <div class="brand"><span class="brand__mark"></span>Quorvent</div>

  <ul class="contacts">
    <li class="contact">
      <span class="contact__icon">
        <svg width="14" height="14" viewBox="0 0 24 24" aria-hidden="true"><path fill="#111" d="M6.6 10.8a15.1 15.1 0 0 0 6.6 6.6l2.2-2.2c.3-.3.7-.4 1-.2 1.1.4 2.3.6 3.6.6.6 0 1 .4 1 1V20c0 .6-.4 1-1 1A17 17 0 0 1 3 4c0-.6.4-1 1-1h3.5c.6 0 1 .4 1 1 0 1.3.2 2.5.6 3.6.1.3 0 .7-.2 1z"/></svg>
      </span>
      <div>
        <p class="contact__label">Phone.</p>
        <p class="contact__value">P: (855) 404-QRVT | M: (813) 555-0192</p>
      </div>
    </li>
    <li class="contact">
      <span class="contact__icon">
        <svg width="14" height="14" viewBox="0 0 24 24" aria-hidden="true" fill="none" stroke="#111" stroke-width="2.6" stroke-linecap="round"><path d="M10 14a4 4 0 0 0 5.7 0l3-3a4 4 0 0 0-5.7-5.7l-1 1"/><path d="M14 10a4 4 0 0 0-5.7 0l-3 3a4 4 0 0 0 5.7 5.7l1-1"/></svg>
      </span>
      <div>
        <p class="contact__label">Email.</p>
        <p class="contact__value">dorian@quorvent.com</p>
      </div>
    </li>
    <li class="contact">
      <span class="contact__icon">
        <svg width="13" height="13" viewBox="0 0 24 24" aria-hidden="true" fill="none" stroke="#111" stroke-width="1.6"><circle cx="12" cy="12" r="10"/><ellipse cx="12" cy="12" rx="4.5" ry="10"/><line x1="2" y1="12" x2="22" y2="12"/><line x1="4" y1="7" x2="20" y2="7"/><line x1="4" y1="17" x2="20" y2="17"/></svg>
      </span>
      <div>
        <p class="contact__label">Website.</p>
        <p class="contact__value">quorvent.com</p>
      </div>
    </li>
  </ul>
</section>

</body>
</html>
```